Re-design existing website and add products for sale.

Our current website is very basic and cluttered. (brightwillowcare.com.au)We want a modern looking website that is easy to navigate. We also want to start selling essential oils and crystal products, so there needs to be a separate page for this. Also needs to be easily edited as we need to change the monthly oracle card with the description. Would like calming colours as we are all about natural healing. Alongside the services listed there should be a button to book now which asks for their name, email, phone number ect. and adds it to the cart.

• Logo is still being designed, please leave a space for the logo which will basically be a lotus flower within a mandala.

```html
<!DOCTYPE html>
<html lang="en">
<head>
<meta charset="utf-8">
<title>Bright Willow Care – Contact</title>
<link href="https://fonts.googleapis.com/css2?family=Open+Sans:wght@700&family=Gabriela&family=Andika:ital@0;1&display=swap" rel="stylesheet">
<style>
  :root {
    --ivory: #fffff0;
    --gold: #cf8f35;
    --gold-line: #d09a50;
    --placeholder: #e0b98f;
    --ink: #111111;
    --card: rgba(255, 255, 255, 0.72);
    --art-light: rgba(240, 215, 175, 0.25);
    --art-deep: rgba(215, 160, 85, 0.35);
  }
  * { box-sizing: border-box; margin: 0; padding: 0; }
  html, body { width: 1200px; height: 1000px; overflow: hidden; }
  body {
    position: relative;
    background: var(--ivory);
    font-family: "Andika", sans-serif;
    color: var(--ink);
  }
  .lotus-art {
    position: absolute;
    left: 0; top: 390px;
    width: 1200px; height: 610px;
    background: linear-gradient(180deg, rgba(255,255,240,0) 0%, var(--art-light) 30%, var(--art-deep) 100%);
  }
  .site-nav { position: absolute; top: 30px; left: 0; width: 1200px; height: 30px; }
  .nav-link {
    position: absolute; top: 0;
    width: 192px; height: 30px;
    background: var(--gold);
    color: #fff;
    font-family: "Open Sans", sans-serif;
    font-weight: 700; font-size: 17px;
    line-height: 30px; text-align: center;
    text-decoration: none;
  }
  .nav-home { left: 110px; }
  .nav-services { left: 308px; }
  .nav-about { left: 700px; }
  .nav-contact { left: 898px; }
  .logo-space {
    position: absolute; top: 18px; left: 500px; width: 200px;
    text-align: center;
    font-family: "Open Sans", sans-serif; font-weight: 700; font-size: 44px;
    line-height: 56px; color: #000;
  }
  .hero { position: absolute; top: 132px; left: 0; width: 1200px; text-align: center; font-family: "Gabriela", serif; }
  .hero-title { font-size: 66px; font-weight: 400; line-height: 80px; }
  .hero-tagline { font-size: 33px; font-weight: 400; line-height: 40px; margin-top: 2px; }
  .contact-card {
    position: absolute; left: 140px; top: 285px;
    width: 920px; height: 562px;
    background: var(--card);
    box-shadow: 0 2px 6px rgba(0,0,0,0.25);
  }
  .field {
    position: absolute;
    border: 1px solid var(--gold-line);
    background: rgba(255,255,255,0.9);
    font-family: "Andika", sans-serif; font-style: italic;
    font-size: 19px; color: var(--placeholder);
    padding: 6px 9px;
  }
  .field-name { left: 155px; top: 30px; width: 300px; height: 40px; }
  .field-email { left: 155px; top: 80px; width: 300px; height: 40px; }
  .field-subject { left: 155px; top: 130px; width: 300px; height: 40px; }
  .field-message { left: 465px; top: 30px; width: 300px; height: 140px; }
  .contact-details {
    position: absolute; left: 0; top: 193px; width: 920px;
    text-align: center; font-size: 30px; line-height: 36px;
  }
  .contact-details p + p { margin-top: 34px; }
  .social-links { position: absolute; top: 467px; left: 333px; width: 254px; height: 64px; }
  .social-dot {
    position: absolute; top: 0;
    width: 64px; height: 64px; border-radius: 50%;
    background: var(--gold);
  }
  .social-one { left: 0; }
  .social-two { left: 95px; }
  .social-three { left: 189px; }
</style>
</head>
<body>
  <div class="lotus-art" role="img" aria-label="Line illustration of lotus flowers and seed pods in gold ink across the lower page"></div>

  <nav class="site-nav">
    <a class="nav-link nav-home" href="#">HOME</a>
    <a class="nav-link nav-services" href="#">SERVICES</a>
    <a class="nav-link nav-about" href="#">ABOUT</a>
    <a class="nav-link nav-contact" href="#">CONTACT</a>
  </nav>
  <div class="logo-space">LOGO</div>

  <header class="hero">
    <h1 class="hero-title">Bright Willow Care</h1>
    <h2 class="hero-tagline">Find Your True Self &amp; Bring Balance To Your Life</h2>
  </header>

  <section class="contact-card">
    <div class="field field-name">Name</div>
    <div class="field field-email">Email</div>
    <div class="field field-subject">Subject</div>
    <div class="field field-message">Message</div>

    <div class="contact-details">
      <p>Tel: 0400 218 764</p>
      <p>42 Linden Street<br>Kensington, SA 5068</p>
      <p>hello@brightwillowcare.com.au</p>
    </div>

    <div class="social-links">
      <span class="social-dot social-one" aria-label="Social link"></span>
      <span class="social-dot social-two" aria-label="Social link"></span>
      <span class="social-dot social-three" aria-label="Social link"></span>
    </div>
  </section>
</body>
</html>
```